Plumbing Business Card Design

our business is a plumbing business.
we would like to see designs with our LOGO featured and then either purple or black writing with a white back ground
or black back ground with white or purple writing or even a purple card!
one option we would love to see is if you could get the TKR letters away from the white background ( it is currently in a white box as a jpeg )it is currently on and overlay it onto black.
FRONT
TKR image to be displayed on the front, please use the attached picture. ( you can remove the email address and mobile number from the botttom and re write it in different font or in a different place on the front.
Directly under the large TKR we would like the words Tidewell Kern Plumbing.
could be spread out like this T I D E W E L L K E R N
P L U M B I N G
We really are open to suggestions though!
Also on the front of the card we could like our little catch phrase somewhere Brindle's Local Plumber

we dont want in plumbing pictures or photos but we are open to swirl across the card or water movement or droplets.

BACK
These services need to be dot pointed or listed on the back
Hot & Cold Water Services
Gas Fitting
Bathroom & Kitchen Renovations
Metal Roofing & Guttering
New Homes & Extensions
Hot Water Service Changeovers
Drainage & Stormwater Works
All General Plumbing & Maitenance

in smaller writing or down the bottom of the card on the back please display write this Lic. No 473918

Contact Information for Business Card

Colm Kern
Mobile: 0427 391 206
email: tidewellkernplumbing@mailnest.example
FInd Us on Facebook Tidewell Kern Plumbing ( with the f symbol ) either on the front or the back

```html
<!DOCTYPE html>
<html lang="en">
<head>
<meta charset="utf-8">
<title>Tidewell Kern Plumbing – Business Cards</title>
<link href="https://fonts.googleapis.com/css2?family=Open+Sans:wght@400;600;700;800&display=swap" rel="stylesheet">
<style>
  :root {
    --brand-purple: #6a2bd9;
    --card-white: #ffffff;
    --ink: #1c1c1c;
    --page-bg: #ecebe8;
  }
  * { box-sizing: border-box; margin: 0; padding: 0; }
  html, body { width: 1200px; height: 900px; overflow: hidden; }
  body {
    position: relative;
    background: var(--page-bg);
    font-family: "Open Sans", Arial, sans-serif;
  }
  .card {
    position: absolute;
    border-radius: 16px;
    overflow: hidden;
    box-shadow: 0 6px 18px rgba(0,0,0,0.18);
  }
  .card-front { left: 78px; top: 34px; width: 588px; height: 364px; background: var(--card-white); }
  .card-back  { left: 389px; top: 505px; width: 566px; height: 351px; background: var(--brand-purple); }

  .band { position: absolute; left: 0; width: 100%; }
  .card-front .band { top: 29px; height: 99px; background: var(--brand-purple); }
  .card-back .band  { top: 82px; height: 97px; background: var(--card-white); }

  .logo-pill {
    position: absolute;
    display: flex; flex-direction: column; align-items: center; justify-content: center;
    border-radius: 70px;
    font-weight: 800;
    text-align: center;
  }
  .card-front .logo-pill { left: 134px; top: 8px; width: 313px; height: 124px; background: var(--card-white); color: var(--brand-purple); }
  .card-back .logo-pill  { left: 152px; top: 78px; width: 258px; height: 106px; background: var(--brand-purple); color: var(--card-white); }
  .logo-initials { font-size: 64px; line-height: 1; letter-spacing: 6px; }
  .card-back .logo-initials { font-size: 54px; }
  .logo-name { font-size: 15px; line-height: 1.2; margin-top: 4px; letter-spacing: 0.2px; }
  .card-back .logo-name { font-size: 13px; }

  .contact {
    position: absolute; left: 0; top: 160px; width: 100%;
    text-align: center; color: var(--ink);
  }
  .contact-name { color: var(--brand-purple); font-size: 21px; font-weight: 700; letter-spacing: 0.5px; line-height: 30px; }
  .tagline { color: var(--brand-purple); font-size: 14px; font-weight: 600; margin-top: 2px; line-height: 20px; }
  .licence { font-size: 16px; margin-top: 12px; line-height: 22px; }
  .licence b { font-weight: 700; }
  .contact-list { list-style: none; margin-top: 14px; font-size: 16px; line-height: 25px; }
  .contact-list li { display: flex; align-items: center; justify-content: center; gap: 5px; }
  .contact-icon { width: 12px; height: 12px; flex: none; }
  .social-mark { width: 12px; height: 12px; border-radius: 2px; background: var(--brand-purple); flex: none; }

  .services {
    position: absolute; left: 0; top: 228px; width: 100%;
    list-style: none; text-align: center;
    color: var(--card-white); font-size: 15px; font-weight: 600; line-height: 23.5px;
  }
  .services .sep { margin: 0 8px; font-weight: 400; }
</style>
</head>
<body>

<section class="card card-front" aria-label="Business card front">
  <div class="band"></div>
  <div class="logo-pill">
    <span class="logo-initials">TKR</span>
    <span class="logo-name">TIDEWELL KERN PLUMBING</span>
  </div>
  <div class="contact">
    <p class="contact-name">COLM KERN</p>
    <p class="tagline">Brindle's Local Plumber</p>
    <p class="licence"><b>Lic. No</b> 473918</p>
    <ul class="contact-list">
      <li>
        <svg class="contact-icon" viewBox="0 0 24 24" aria-hidden="true"><path fill="#6a2bd9" d="M6.6 10.8a15.1 15.1 0 0 0 6.6 6.6l2.2-2.2a1 1 0 0 1 1-.25 11.4 11.4 0 0 0 3.6.57 1 1 0 0 1 1 1V20a1 1 0 0 1-1 1A17 17 0 0 1 3 4a1 1 0 0 1 1-1h3.5a1 1 0 0 1 1 1c0 1.25.2 2.45.57 3.57a1 1 0 0 1-.25 1z"/></svg>
        0427 391 206
      </li>
      <li>
        <svg class="contact-icon" viewBox="0 0 24 24" aria-hidden="true"><rect x="2" y="5" width="20" height="14" fill="#6a2bd9"/><path d="M2 5l10 8 10-8" fill="none" stroke="#fff" stroke-width="1.8"/></svg>
        tidewellkernplumbing@mailnest.example
      </li>
      <li><span class="social-mark" aria-hidden="true"></span>TidewellKernPlumbing</li>
    </ul>
  </div>
</section>

<section class="card card-back" aria-label="Business card back">
  <div class="band"></div>
  <div class="logo-pill">
    <span class="logo-initials">TKR</span>
    <span class="logo-name">TIDEWELL KERN PLUMBING</span>
  </div>
  <ul class="services">
    <li>Hot &amp; Cold Water Services<span class="sep">|</span>Gas Fitting</li>
    <li>Bathroom &amp; Kitchen Renovations<span class="sep">|</span>Metal Roofing &amp; Guttering</li>
    <li>New Homes &amp; Extensions<span class="sep">|</span>Hot Water Service Changeovers</li>
    <li>Drainage &amp; Stormwater Works<span class="sep">|</span>All General Plumbing &amp; Maitenance</li>
  </ul>
</section>

</body>
</html>
```